Business Card Design Project

New Business Card design for Varodine Technology Ltd using new Logo and new Tagline for staffing company.

About us from our website - www.varodine.example:

VaroDine is a leading and recognized Electronic Entertainment, Workforce Augmentation, and Project Management solutions provider with clients in Electronic Entertainment, Legal, Technology, Government and other verticals that range in size from start up organizations to Zenlar 500 companies. VaroDine is certified as an 8(a) minority and woman owned enterprise, established in 1998.

Target Market(s)

Companies in Electronic Entertainment, Legal, Government and Technology

Industry/Entity Type

Business

Requirements
Must have
• Must include in small letters the following information on back:

Established in 1998
8(a)(w)(e), Cage #7KRT9, DUNS #462137580

Front should have the following:
Derek Holloway
Vice President
5820 Birchmont Road
Fallowby, FB 482917
555-318-2746 X 100
555-902-6613 Fax
555-318-2746 Toll Free
name@varodine.example

Our Tagline: Connect • Collaborate • Achieve

```html
<!DOCTYPE html>
<html lang="en">
<head>
<meta charset="utf-8">
<title>VaroDine Business Card</title>
<link href="https://fonts.googleapis.com/css2?family=Open+Sans:wght@300;400;600;700&display=swap" rel="stylesheet">
<style>
  :root {
    --page-bg: #e6e7e9;
    --card-deep: #0b2a5c;
    --card-mid: #14489a;
    --card-glow: #1f63c4;
    --white: #ffffff;
    --soft-white: rgba(255, 255, 255, 0.82);
    --logo-ink: #3a4a5a;
    --title-blue: #5b93d6;
    --name-band: rgba(4, 18, 48, 0.55);
  }
  * { margin: 0; padding: 0; box-sizing: border-box; }
  html, body {
    width: 1200px; height: 900px; overflow: hidden;
    background: var(--page-bg);
    font-family: "Open Sans", Arial, sans-serif;
  }
  .canvas { position: relative; width: 1200px; height: 900px; }

  .card {
    position: absolute;
    width: 700px; height: 400px;
    left: 250px;
    overflow: hidden;
    background: radial-gradient(ellipse at 35% 30%, var(--card-glow) 0%, var(--card-mid) 35%, var(--card-deep) 100%);
    box-shadow: 0 6px 18px rgba(0,0,0,0.25);
  }
  .card--back { top: 36px; }
  .card--front {
    top: 464px;
    background: radial-gradient(ellipse at 40% 55%, var(--card-glow) 0%, var(--card-mid) 38%, var(--card-deep) 100%);
  }

  /* Back side */
  .logo-panel {
    position: absolute;
    left: 395px; top: 150px;
    width: 305px; height: 96px;
    background: var(--white);
    display: flex; align-items: center; gap: 14px;
    padding-left: 34px;
  }
  .logo-dot { width: 26px; height: 26px; border-radius: 50%; background: var(--card-mid); }
  .logo-name { font-size: 40px; font-weight: 600; color: var(--logo-ink); letter-spacing: -0.5px; }
  .back-details {
    position: absolute; right: 26px; top: 262px;
    text-align: right; color: var(--white);
  }
  .established { font-size: 21px; font-weight: 600; line-height: 30px; }
  .tagline { font-size: 13px; font-weight: 400; color: var(--soft-white); margin-top: 6px; letter-spacing: 0.3px; }
  .registration { font-size: 11px; font-weight: 400; color: var(--soft-white); margin-top: 3px; }

  /* Front side */
  .identity {
    position: absolute;
    left: 60px; top: 340px;
    transform-origin: 0 0;
    transform: rotate(-36deg);
    width: 640px; height: 112px;
  }
  .name-line { position: absolute; left: 0; top: 0; display: flex; align-items: flex-end; gap: 10px; }
  .name-first {
    background: var(--name-band);
    color: var(--white); font-weight: 700; font-size: 40px;
    padding: 0 12px; line-height: 56px;
  }
  .name-last { color: var(--white); font-weight: 300; font-size: 40px; line-height: 56px; }
  .plug-mark {
    width: 54px; height: 54px; border-radius: 50%;
    background: var(--white);
    margin-left: 6px;
  }
  .job-title {
    position: absolute; left: 140px; top: 58px;
    color: var(--title-blue); font-weight: 300; font-size: 36px; line-height: 50px;
    white-space: nowrap;
  }
  .contact {
    position: absolute; left: 430px; top: 8px;
    list-style: none;
    color: var(--white); font-size: 12.5px; line-height: 17px; font-weight: 400;
    white-space: nowrap;
  }
</style>
</head>
<body>
<main class="canvas">
  <section class="card card--back" aria-label="Card back">
    <div class="logo-panel">
      <span class="logo-dot"></span>
      <span class="logo-name">VaroDine</span>
    </div>
    <div class="back-details">
      <p class="established">Established in 1998</p>
      <p class="tagline">Connect • Collaborate • Achieve</p>
      <p class="registration">8(a)(w)(e), Cage #7KRT9, DUNS #462137580</p>
    </div>
  </section>

  <section class="card card--front" aria-label="Card front">
    <div class="identity">
      <div class="name-line">
        <span class="name-first">Derek</span>
        <span class="name-last">Holloway</span>
        <span class="plug-mark" role="img" aria-label="Power plug illustration"></span>
      </div>
      <p class="job-title">Vice President</p>
      <ul class="contact">
        <li>5820 Birchmont Road</li>
        <li>Fallowby, FB 482917</li>
        <li>555-318-2746 X 100</li>
        <li>555-902-6613 Fax</li>
        <li>555-318-2746 Toll Free</li>
        <li>name@varodine.example</li>
      </ul>
    </div>
  </section>
</main>
</body>
</html>
```